Plate Bright Class (workshop to teach people to eat fruits and vegetables)

Double sided DL Flyer

Free Community Workshop
Plate Bright Live Light
Central Coast NSW

Copy to appear on flyer side one:-
PLATE BRIGHT LIVE LIGHT
interactive workshops
March-April 2019
Presented by qualified nutritionist

Food for healthier happier life for you and your family (free to central coast residents - all ages welcome

Side 2
Learn About:-
Foods that improve your health
basic nutrition
gut brain connection
portion size
menu planning
preparation
eating

Benefits
Improved health
Improved Energy
Manage chronic illness
diabetes type II
cholesterol
Blood Pressure
Family fun

Food Tastings
Lucky Door Prize

Reserve for spot online @ www.platebright.com.au or call 0482 916 304
Supported by Harbourview Shire Council (Logo) Tidewater Rovers Club (Logo) Pinebrook Veterans Club (Logo)

I would like to see a flyer that is bright, fun and fresh with images of fresh food.

Target Market(s)

Women 30 plus

Industry/Entity Type

Health And Wellness

Logo Text

PLATE BRIGHT LIVE LIGHT

Font styles to use
Other font styles liked:
• bold clean

Colors
f37122
9bcb3c
fbed22
ec1f27
e34297

Requirements
Must have
• bright eye catching colours featuring fresh fruit and vegetables
• I have attached a some images of designs I like
Nice to have
• Im happy for the designer to change copy to create a clean flyer without loosing essential information
• I like the feel of the banner on my facebook page
• Sunroot Kitchen - Plate Bright Live Light with Delia Frome
• https://www.facebook.com/sunrootkitchenoz/
Should not have
• old fashioned images

```html
<!DOCTYPE html>
<html lang="en">
<head>
<meta charset="utf-8">
<title>Plate Bright Live Light – DL Flyer</title>
<link rel="stylesheet" href="https://fonts.googleapis.com/css2?family=Open+Sans:wght@400;600;700&family=Ubuntu:wght@500;700&display=swap">
<style>
  :root{
    --stage:#a3a3a3;
    --navy:#132131;
    --navy-deep:#0c1622;
    --yellow:#fbed22;
    --orange:#f37122;
    --green:#9bcb3c;
    --red:#ec1f27;
    --pink:#e34297;
    --ink:#1d1d1d;
    --strip:#dcdcdc;
    --white:#ffffff;
    --council:#1d3e6e;
  }
  *{box-sizing:border-box;margin:0;padding:0}
  html,body{width:800px;height:1200px;overflow:hidden}
  body{background:var(--stage);font-family:"Open Sans",sans-serif;position:relative;color:var(--ink)}

  .flyer{position:absolute;left:40px;width:720px;height:360px;overflow:hidden;box-shadow:0 4px 14px rgba(0,0,0,.25)}
  .flyer--front{top:200px;background:radial-gradient(ellipse at 40% 40%,#1f3147 0%,var(--navy) 55%,var(--navy-deep) 100%)}
  .flyer--back{top:640px;background:linear-gradient(135deg,#e9f3d2 0%,#f6faec 45%,#ffffff 100%)}

  /* front */
  .headline{position:absolute;left:22px;top:16px;font-family:"Ubuntu",sans-serif;font-weight:700;font-size:37px;line-height:37px;letter-spacing:.5px;color:var(--yellow)}
  .headline .outline{color:transparent;-webkit-text-stroke:1.3px var(--yellow);font-weight:500}
  .session{position:absolute;left:196px;top:44px;width:290px;height:100px}
  .session svg{position:absolute;inset:0;overflow:visible}
  .session__text{position:absolute;left:28px;top:22px;color:var(--white);font-family:"Ubuntu",sans-serif}
  .session__kind{font-size:20px;font-weight:500;line-height:26px}
  .session__dates{font-size:24px;font-weight:700;line-height:30px}
  .band{position:absolute;left:0;height:22px;padding-left:22px;font-weight:700;font-size:14px;line-height:22px;white-space:nowrap}
  .band--pink{top:176px;width:368px;height:26px;line-height:26px;font-size:15px;background:var(--pink);color:var(--yellow)}
  .band--green{top:216px;width:453px;background:var(--green);color:var(--ink)}
  .band--yellow{top:243px;width:276px;background:var(--yellow);color:var(--ink)}
  .band--orange{top:268px;width:181px;background:var(--orange);color:var(--white)}
  .produce{position:absolute;right:0;top:0;width:250px;height:302px;background:radial-gradient(circle at 55% 45%,#f6a33a 0%,#e4432e 35%,#6fa83a 70%,#24402a 100%)}
  .strip{position:absolute;left:0;right:0;top:302px;height:46px;background:var(--strip);display:flex;justify-content:space-between;align-items:center;padding:0 22px}
  .strip__note{font-size:12px;font-weight:600;line-height:16px;color:var(--ink)}
  .strip__url{font-size:15px;font-weight:600;color:var(--ink)}
  .accent{color:var(--pink)}
  .base{position:absolute;left:0;right:0;bottom:0;height:12px;background:var(--navy-deep)}

  /* back */
  .portrait{position:absolute;right:0;top:0;width:320px;height:250px;background:linear-gradient(90deg,rgba(238,245,224,0) 0%,rgba(217,194,173,.55) 30%,#d9c2ad 50%,#7ca64b 78%,#e5eed6 100%)}
  .tag{position:absolute;top:21px;height:22px;width:144px;background:var(--green);color:var(--red);font-weight:600;font-size:14px;line-height:22px;padding-left:12px}
  .tag--learn{left:25px}
  .tag--benefits{left:274px}
  .checklist{position:absolute;top:50px;list-style:none;font-size:12.5px;line-height:17.5px;color:var(--ink);white-space:nowrap}
  .checklist--learn{left:30px}
  .checklist--benefits{left:279px}
  .checklist li{position:relative;padding-left:16px}
  .checklist li::before{content:"";position:absolute;left:0;top:4px;width:9px;height:9px;border:1.3px solid var(--red);border-radius:50%}
  .checklist li::after{content:"";position:absolute;left:3px;top:5.5px;width:3px;height:5px;border-right:1.3px solid var(--red);border-bottom:1.3px solid var(--red);transform:rotate(40deg)}
  .checklist li.sub{padding-left:32px}
  .checklist li.sub::before{display:none}
  .checklist li.sub::after{left:20px;top:4px;width:4px;height:8px;border-color:var(--red);border-width:1.6px}
  .prizes{position:absolute;left:62px;top:190px;width:258px;height:84px}
  .prizes svg{position:absolute;inset:0;overflow:visible}
  .prizes__text{position:absolute;left:0;right:0;top:16px;text-align:center;color:var(--yellow);font-family:"Ubuntu",sans-serif}
  .prizes__small{font-size:17px;font-weight:500;line-height:22px}
  .prizes__big{font-size:21px;font-weight:700;line-height:27px}
  .footer{position:absolute;left:0;right:0;top:250px;bottom:0;background:var(--white)}
  .reserve{position:absolute;left:27px;top:56px;font-size:15px;font-weight:600;line-height:21px;color:var(--ink)}
  .supporters__title{position:absolute;left:527px;top:24px;font-size:12px;font-weight:700}
  .supporters{position:absolute;left:455px;top:62px;display:flex;gap:16px;align-items:center}
  .supporter{display:flex;align-items:center;gap:5px;font-size:9.5px;font-weight:600;line-height:11px;color:var(--council)}
  .supporter__dot{width:22px;height:22px;border-radius:50%;background:var(--council);flex:none}
</style>
</head>
<body>

<section class="flyer flyer--front" aria-label="Flyer side one">
  <h1 class="headline">PLATE<br>BRIGHT<br><span class="outline">LIVE<br>LIGHT</span></h1>

  <div class="session">
    <svg viewBox="0 0 290 100" aria-hidden="true">
      <polygon points="22,14 270,4 262,78 14,86" fill="var(--orange)"/>
      <polygon points="8,20 282,10 270,92 2,96" fill="none" stroke="var(--orange)" stroke-width="1.5"/>
      <polygon points="150,-2 160,3 150,8" fill="var(--white)"/>
      <polygon points="0,48 -8,44 0,40" fill="var(--white)"/>
      <polygon points="104,96 114,100 104,104" fill="var(--white)"/>
    </svg>
    <div class="session__text">
      <p class="session__kind">Interactive workshops</p>
      <p class="session__dates">March-April 2019</p>
    </div>
  </div>

  <p class="band band--pink">Presented by qualified nutritionist</p>
  <p class="band band--green">Food for healthier happier life for you and your family</p>
  <p class="band band--yellow">free to central coast residents</p>
  <p class="band band--orange">all ages welcome</p>

  <div class="produce" role="img" aria-label="Photo of fresh fruit: oranges, kiwi, grapefruit, grapes, strawberries and leaves"></div>

  <div class="strip">
    <p class="strip__note">Was thinking this could be fruit and vegetables in the shape<br>of a waist with a tape measure measuring the waist</p>
    <p class="strip__url">www.<span class="accent">platebright</span>.com.au</p>
  </div>
  <div class="base"></div>
</section>

<section class="flyer flyer--back" aria-label="Flyer side two">
  <div class="portrait" role="img" aria-label="Photo of a woman eating a fresh salad from a bowl"></div>

  <h2 class="tag tag--learn">Learn About:-</h2>
  <ul class="checklist checklist--learn">
    <li>Foods that improve your health</li>
    <li>basic nutrition</li>
    <li>gut brain connection</li>
    <li>portion size</li>
    <li>menu planning</li>
    <li>preparation</li>
    <li>eating</li>
  </ul>

  <h2 class="tag tag--benefits">Benefits:-</h2>
  <ul class="checklist checklist--benefits">
    <li>Improved Health</li>
    <li>Improved Energy</li>
    <li>Manage Chronic Illness</li>
    <li class="sub">Diabetes Type II</li>
    <li class="sub">Cholesterol</li>
    <li class="sub">Blood Pressure</li>
    <li>Family fun</li>
  </ul>

  <div class="footer">
    <p class="reserve">Reserve for spot online @ www.<span class="accent">platebright</span>.com.au<br>or call <span class="accent">0482 916 304</span></p>
    <p class="supporters__title">Supported by</p>
    <div class="supporters">
      <div class="supporter"><span class="supporter__dot"></span>Harbourview<br>Shire Council</div>
      <div class="supporter">Tidewater<br>Rovers Club</div>
      <div class="supporter">Pinebrook<br>Veterans Club</div>
    </div>
  </div>

  <div class="prizes">
    <svg viewBox="0 0 258 84" aria-hidden="true">
      <polygon points="14,10 250,2 242,72 6,78" fill="var(--pink)"/>
      <polygon points="22,4 256,12 246,82 2,74" fill="none" stroke="var(--pink)" stroke-width="1.3"/>
      <polygon points="0,40 -8,36 0,32" fill="var(--green)" transform="translate(8,0)"/>
      <polygon points="180,80 190,84 180,88" fill="var(--green)"/>
    </svg>
    <div class="prizes__text">
      <p class="prizes__small">Food Tastings</p>
      <p class="prizes__big">Lucky Door Prize</p>
    </div>
  </div>
</section>

</body>
</html>
```